Banner Ad for Resume Services Website

The add is for this web site: www.BrightFolioDesk.com

The site offers 4 different services:

- Resume Writing (by a Certified Professional Resume Writer)
- Resume Posting (posts your resume to 85 job sites)
- Resume Distribution (sends your resume to hundreds of recruiters)
- Resume Online website (created an online resume with a domain name to your name)

Colors to be used are Blue, Yellow, etc... please check the website for inspiration.

Check the web site to learn more.

Target Market(s)

Unemployed, Professionals who want to switch jobs, etc..

Industry/Entity Type

Learn

Requirements
Must have
• We definitely one this to be included on the banner:

"Free Resume Samples"

in order to attract clicks.
Nice to have
• Some of the words we suggest to include on the banner are:

"How Good is Your Resume? Ask a Professional !"

Should not have
• No animation !

Do not place the LOGO on the banner as our LOGO might change in the near future. If you already submitted a banner with the LOGO on it, you can replace it with any other graphic that has a Resume/Jobs/BusinessStaff related theme.

```html
<!DOCTYPE html>
<html lang="en">
<head>
<meta charset="utf-8">
<title>Resume Services Banner</title>
<link rel="stylesheet" href="https://fonts.googleapis.com/css2?family=Arimo:wght@700&display=swap">
<style>
  :root {
    --blue-deep: #06205e;
    --blue-mid: #1a54b4;
    --blue-bright: #3f95e6;
    --blue-pale: #8cc6f2;
    --text-yellow: #f7d731;
    --star-yellow: #f6c300;
    --button-yellow: #ffd21c;
    --ink: #0b0b0b;
  }
  html, body {
    margin: 0;
    padding: 0;
    overflow: hidden;
    background: #ffffff;
  }
  .banner {
    position: relative;
    width: 1200px;
    height: 148px;
    overflow: hidden;
    font-family: "Arimo", Arial, sans-serif;
  }
  .banner__texture {
    position: absolute;
    inset: 0;
    background:
      radial-gradient(ellipse 420px 160px at 930px 70px, var(--blue-pale) 0%, rgba(140,198,242,0) 70%),
      radial-gradient(ellipse 300px 120px at 560px 120px, rgba(63,149,230,0.8) 0%, rgba(63,149,230,0) 70%),
      linear-gradient(100deg, var(--blue-deep) 0%, var(--blue-mid) 40%, var(--blue-bright) 70%, var(--blue-mid) 100%);
  }
  .services {
    position: absolute;
    left: 10px;
    top: 14px;
    margin: 0;
    padding: 0;
    list-style: none;
  }
  .services__item {
    display: flex;
    align-items: center;
    height: 39px;
    font-size: 21px;
    color: var(--text-yellow);
    text-shadow: 1px 1px 0 var(--ink), -1px 0 0 rgba(0,0,0,0.6);
    white-space: nowrap;
  }
  .services__star {
    width: 26px;
    height: 26px;
    margin-right: 8px;
    flex: none;
  }
  .cta-button {
    position: absolute;
    left: 799px;
    top: 36px;
    width: 376px;
    height: 79px;
    box-sizing: border-box;
    border: 3px solid var(--ink);
    border-radius: 14px;
    background: linear-gradient(180deg, #ffe14a 0%, var(--button-yellow) 55%, #f2bf00 100%);
    display: flex;
    align-items: center;
    justify-content: center;
    font-size: 31px;
    color: var(--ink);
    text-decoration: none;
  }
</style>
</head>
<body>
  <div class="banner">
    <div class="banner__texture" role="img" aria-label="Blue grunge splatter texture background"></div>

    <ul class="services">
      <li class="services__item">
        <svg class="services__star" viewBox="0 0 24 24" aria-hidden="true"><polygon points="12,1 15,9 23,9 16.5,14 19,22 12,17 5,22 7.5,14 1,9 9,9" fill="var(--star-yellow)" stroke="#8a5a00" stroke-width="0.8"/></svg>
        Resume Writing (by a Certified Professional Resume Writer)
      </li>
      <li class="services__item">
        <svg class="services__star" viewBox="0 0 24 24" aria-hidden="true"><polygon points="12,1 15,9 23,9 16.5,14 19,22 12,17 5,22 7.5,14 1,9 9,9" fill="var(--star-yellow)" stroke="#8a5a00" stroke-width="0.8"/></svg>
        Resume Posting (posts your resume to 85 job sites)
      </li>
      <li class="services__item">
        <svg class="services__star" viewBox="0 0 24 24" aria-hidden="true"><polygon points="12,1 15,9 23,9 16.5,14 19,22 12,17 5,22 7.5,14 1,9 9,9" fill="var(--star-yellow)" stroke="#8a5a00" stroke-width="0.8"/></svg>
        Resume Distribution (sends your resume to hundreds of recruiters)
      </li>
    </ul>

    <a class="cta-button" href="#">Free Resume Samples</a>
  </div>
</body>
</html>
```